Independent IT Consulting Professional. Looking for a clean crisp, somewhat traditional design. I have also attached the initial off-the-shelf design from PrintHaven. My company has grown quickly, and I would like to take the card to the next level. Should be sharp, mature, classy well laid-out and convey confidence. I don't think the off-the-shelf design does this. I like the logo I have for the time being, but if someone has something better in mind, I would be happy to consider an alternative. I would also like to see the color Cyan used in a small way, either with the logo or some other color treatment, as I feel like this is a modern color that I always liked, but never was able to make anything work with it.
Industry/Entity Type
It Company
Contact Information for Business Card
Carter J. Whitlow
Owner
TrellMark Solutions
2817 Ashborough Lane
Harlow Falls, NY 13990
(645) 555-0148
cwhitlow@trellmarksolutions.example
www.trellmarksolutions.example
Tagline: Business Technology Services and Consulting

```html
<!DOCTYPE html>
<html lang="en">
<head>
<meta charset="utf-8">
<title>TrellMark Solutions – Business Card</title>
<link rel="stylesheet" href="https://fonts.googleapis.com/css2?family=Alegreya+Sans:ital,wght@0,400;0,800;1,400&family=Quicksand:wght@700&family=Open+Sans:wght@400&display=swap">
<style>
  :root {
    --backdrop: #4a4a4a;
    --card-white: #ffffff;
    --card-tint: #e2f0fb;
    --brand-blue: #2b5cab;
    --name-blue: #1f4fa0;
    --ink: #1b1b1b;
    --cyan: #19b5e6;
    --band-text: #ffffff;
  }
  * { margin: 0; padding: 0; box-sizing: border-box; }
  html, body {
    width: 1200px; height: 900px; overflow: hidden;
    background: var(--backdrop);
  }
  .business-card {
    position: absolute; left: 75px; top: 150px;
    width: 1050px; height: 600px;
    background: var(--card-tint);
    box-shadow: 0 20px 40px rgba(0,0,0,.45);
    overflow: hidden;
  }
  .card-top {
    position: absolute; left: 0; top: 0; width: 100%; height: 225px;
    background: var(--card-white);
  }
  .brand {
    position: absolute; left: 70px; top: 55px;
    display: flex; align-items: center; gap: 18px;
  }
  .brand-dot {
    width: 22px; height: 22px; border-radius: 50%;
    background: var(--cyan);
  }
  .brand-name {
    font-family: "Alegreya Sans", sans-serif; font-weight: 800;
    font-size: 46px; line-height: 1.0; color: var(--ink);
  }
  .person {
    position: absolute; right: 70px; top: 125px; text-align: center;
  }
  .person-name {
    font-family: "Quicksand", sans-serif; font-weight: 700;
    font-size: 40px; color: var(--name-blue); letter-spacing: .5px;
  }
  .person-title {
    font-family: "Alegreya Sans", sans-serif; font-style: italic;
    font-size: 28px; color: var(--ink); margin-top: 2px;
  }
  .tagline-band {
    position: absolute; left: 0; top: 225px; width: 100%; height: 48px;
    background: var(--brand-blue);
    display: flex; align-items: center; padding-left: 40px;
  }
  .tagline {
    font-family: "Open Sans", sans-serif; font-size: 32px;
    color: var(--band-text); letter-spacing: .3px;
  }
  .contact-list {
    position: absolute; right: 45px; top: 300px;
    list-style: none;
  }
  .contact-item {
    display: flex; align-items: center; justify-content: flex-end;
    gap: 22px; height: 58px; white-space: nowrap;
    font-family: "Alegreya Sans", sans-serif; font-size: 34px; color: var(--ink);
  }
  .contact-icon { width: 30px; height: 30px; flex: none; fill: var(--brand-blue); }
</style>
</head>
<body>
  <section class="business-card">
    <div class="card-top">
      <div class="brand">
        <span class="brand-dot"></span>
        <span class="brand-name">TrellMark<br>Solutions</span>
      </div>
      <div class="person">
        <div class="person-name">Carter J. Whitlow</div>
        <div class="person-title">Owner</div>
      </div>
    </div>

    <div class="tagline-band">
      <span class="tagline">Business Technology Services and Consulting</span>
    </div>

    <ul class="contact-list">
      <li class="contact-item">(645) 555-0148
        <svg class="contact-icon" viewBox="0 0 24 24" aria-hidden="true"><path d="M7 1h10a2 2 0 0 1 2 2v18a2 2 0 0 1-2 2H7a2 2 0 0 1-2-2V3a2 2 0 0 1 2-2zm0 3v9h10V4zm1 11v2h2v-2zm3 0v2h2v-2zm3 0v2h2v-2zm-6 3v2h2v-2zm3 0v2h2v-2zm3 0v2h2v-2z"/></svg>
      </li>
      <li class="contact-item">cwhitlow@trellmarksolutions.example
        <svg class="contact-icon" viewBox="0 0 24 24" aria-hidden="true"><path d="M2 5h20v14H2zm2 2v.5l8 5.5 8-5.5V7l-8 5.2z"/></svg>
      </li>
      <li class="contact-item">www.trellmarksolutions.example
        <svg class="contact-icon" viewBox="0 0 24 24" aria-hidden="true"><path d="M12 2a10 10 0 1 0 0 20 10 10 0 0 0 0-20zm-1 2.1V6L9 8l1 2-3 1-2.8-1.6A8 8 0 0 1 11 4.1zM13 20v-3l3-2-1-3 4-1 .9 1A8 8 0 0 1 13 20z"/></svg>
      </li>
      <li class="contact-item">2817 Ashborough Lane Harlow Falls, NY 13990
        <svg class="contact-icon" viewBox="0 0 24 24" aria-hidden="true"><path d="M12 1a8 8 0 0 0-8 8c0 6 8 14 8 14s8-8 8-14a8 8 0 0 0-8-8zm0 11a3 3 0 1 1 0-6 3 3 0 0 1 0 6z"/></svg>
      </li>
    </ul>
  </section>
</body>
</html>
```